Business card

We are looking for a creative person to deigns our company business card.

Target Market(s)

College age student

Industry/Entity Type

Accommodation

Contact Information for Business Card

We want a fun, clean and sophisticated design. It should look good, but more importantly the information should be legible.

Font styles to use
Serif
Sans Serif
Other font styles liked:
• Open Sans ,

Colors
33a6d7

Requirements
Must have
• Must have a young and memorable message. Be legible.
• Our logo on the back on a solid blue , please find color and logo attached
• LodgeBridgely.net on the back.
Nice to have
• I would like to have couple of different fonts on the LodgeBridgely.net on the back of the cards with a solid blue.

```html
<!DOCTYPE html>
<html lang="en">
<head>
<meta charset="utf-8">
<title>LodgeBridgely Business Card</title>
<link href="https://fonts.googleapis.com/css2?family=Open+Sans:wght@400;600;700&display=swap" rel="stylesheet">
<style>
  :root {
    --brand-blue: #2b93d4;
    --brand-blue-light: #33a6d7;
    --brand-blue-deep: #1f6fb4;
    --navy: #0f3f78;
    --card-white: #ffffff;
    --page-bg: #e9ecef;
  }
  * { margin: 0; padding: 0; box-sizing: border-box; }
  html, body { width: 1200px; height: 1200px; overflow: hidden; }
  body {
    background: var(--page-bg);
    font-family: "Open Sans", Arial, sans-serif;
    display: flex; flex-direction: column; align-items: center; justify-content: center;
    gap: 64px;
  }
  .card {
    width: 900px; height: 514px; position: relative; overflow: hidden;
    box-shadow: 0 6px 20px rgba(0,0,0,.15);
  }

  /* Front */
  .card-front { background: var(--card-white); }
  .name-band {
    position: absolute; left: 0; top: 38px; width: 640px; height: 66px;
    background: var(--brand-blue);
    display: flex; align-items: center; padding-left: 44px;
  }
  .name-band::after {
    content: ""; position: absolute; right: 0; bottom: -6px; width: 640px; height: 6px; background: var(--navy);
  }
  .name-tick { width: 6px; height: 40px; background: var(--card-white); margin-right: 18px; }
  .person-name { color: var(--card-white); font-weight: 700; font-size: 38px; letter-spacing: .5px; }
  .person-role {
    position: absolute; left: 44px; top: 122px;
    color: var(--navy); font-weight: 700; font-size: 26px;
  }
  .contact-list { position: absolute; left: 44px; top: 190px; list-style: none; }
  .contact-item {
    display: flex; align-items: center; gap: 18px; margin-bottom: 22px;
    color: var(--navy); font-weight: 600; font-size: 22px;
  }
  .contact-icon { width: 40px; height: 40px; flex: none; }
  .front-brand {
    position: absolute; right: 60px; top: 250px;
    display: flex; align-items: center; gap: 12px;
    color: var(--brand-blue-deep); font-weight: 700; font-size: 30px;
  }
  .brand-square { width: 22px; height: 22px; background: var(--brand-blue); }
  .bottom-band {
    position: absolute; left: 0; bottom: 0; width: 100%; height: 62px; background: var(--brand-blue);
  }
  .bottom-band::before {
    content: ""; position: absolute; left: 0; top: -14px; width: 100%; height: 6px; background: var(--navy);
  }

  /* Back */
  .card-back {
    background: linear-gradient(180deg, var(--brand-blue-deep) 0%, var(--brand-blue) 45%, var(--brand-blue-deep) 100%);
    display: flex; flex-direction: column; align-items: center;
  }
  .back-brand {
    margin-top: 205px;
    display: flex; align-items: center; gap: 14px;
    color: var(--card-white); font-weight: 700; font-size: 44px;
  }
  .back-brand .brand-square { background: var(--card-white); width: 30px; height: 30px; }
  .back-address {
    position: absolute; bottom: 74px; width: 100%; text-align: center;
    color: var(--card-white); font-size: 17px; font-weight: 600; letter-spacing: .2px;
  }
</style>
</head>
<body>

<section class="card card-front">
  <div class="name-band">
    <span class="name-tick"></span>
    <span class="person-name">John Doe</span>
  </div>
  <p class="person-role">Managing Partner</p>

  <ul class="contact-list">
    <li class="contact-item">
      <svg class="contact-icon" viewBox="0 0 40 40" aria-hidden="true">
        <circle cx="20" cy="20" r="20" fill="#0f3f78"/>
        <path d="M14 11c1.5-1 3 0 3.6 1.6l1 2.6c.4 1-.2 2-1 2.5l-1 .7c.9 2.3 2.5 4 4.8 5l.7-1c.5-.8 1.6-1.3 2.5-.9l2.6 1c1.6.7 2.5 2.1 1.6 3.6-1.5 2.4-4 3-6.5 2-5-2-8.7-5.7-10.4-10.6-.8-2.5-.3-4.9 2.1-6.5z" fill="#fff"/>
      </svg>
      <span>000.000.0000</span>
    </li>
    <li class="contact-item">
      <svg class="contact-icon" viewBox="0 0 40 40" aria-hidden="true">
        <circle cx="20" cy="20" r="20" fill="#0f3f78"/>
        <rect x="10" y="13" width="20" height="14" fill="#fff"/>
        <path d="M10 13l10 8 10-8" fill="none" stroke="#0f3f78" stroke-width="2"/>
      </svg>
      <span>sample@lodgemail.net</span>
    </li>
    <li class="contact-item">
      <svg class="contact-icon" viewBox="0 0 40 40" aria-hidden="true">
        <circle cx="20" cy="20" r="20" fill="#0f3f78"/>
        <g fill="none" stroke="#fff" stroke-width="2">
          <circle cx="20" cy="20" r="10"/>
          <ellipse cx="20" cy="20" rx="4.5" ry="10"/>
          <line x1="10" y1="20" x2="30" y2="20"/>
          <line x1="12" y1="14" x2="28" y2="14"/>
          <line x1="12" y1="26" x2="28" y2="26"/>
        </g>
      </svg>
      <span>https://lodgebridgely.net</span>
    </li>
  </ul>

  <div class="front-brand">
    <span class="brand-square"></span>
    <span>LodgeBridgely</span>
  </div>

  <div class="bottom-band"></div>
</section>

<section class="card card-back">
  <div class="back-brand">
    <span class="brand-square"></span>
    <span>LodgeBridgely</span>
  </div>
  <p class="back-address">218 Marlow Ave., Suite 307, Los Angeles, California CA 90031</p>
</section>

</body>
</html>
```